Kobalto Cell Phone Repair

We are a small cell phone repair store in need of a redesign to our current business card to make it a more modern, cleaner design that will catch folks' attention (perhaps with rounded edges ) - But still include most of the information listed on the current card. Would like to keep the current color scheme of black/white and green. Card will not need any personnel name included. Would like to see some designs include takes on a velorin or tekvo screen as well as more traditional cards.

Target Market(s)

broad spectrum across all cell phone users

Industry/Entity Type

Cell Phone

Contact Information for Business Card

changes to front text:
keep business Logo
business address, phone number website and email. All other info optional (add gathernest and blurvo icons on card

Rear of card:

Keep repair services, change tekvo repair to slatra repair, change quorvex os repair to data recovery (with appropriate icon or substitute)
remove products text
remove pjw and ravesh from manufacturer logos, add dunbelio.

Requirements
Must have
• business Logo
• business address, phone number website and email
• keep colors to white/black/green/gray
• gathernest and blurvo icons on card
Nice to have
• Would like to see 'traditional' business card design as well as creative design incorporating incorporating front of cell phone (eg tekvo or quorvex). Rounded edges would be nice but not necessary.

```html
<!DOCTYPE html>
<html lang="en">
<head>
<meta charset="utf-8">
<title>Kobalto Cell Phone Repair — Services Card</title>
<link rel="stylesheet" href="https://fonts.googleapis.com/css2?family=Open+Sans:wght@300;400;700&display=swap">
<style>
  :root {
    --paper: #ffffff;
    --frame: #4b4b4d;
    --ink: #1a1a1a;
    --brand-ink: #3d3d3f;
    --accent: #7ab842;
    --trim: #e2e2e2;
    --mark: #000000;
  }
  html, body {
    margin: 0;
    padding: 0;
    width: 1200px;
    height: 804px;
    overflow: hidden;
    background: var(--paper);
  }
  .print-sheet { display: block; width: 1200px; height: 804px; }
  .crop-mark { stroke: var(--mark); stroke-width: 1; }
  .reg-ring { fill: none; stroke: var(--mark); stroke-width: 1.5; }
  .reg-dot { fill: var(--mark); }
  .reg-cross { stroke: var(--paper); stroke-width: 2; }
  .reg-line { stroke: var(--mark); stroke-width: 1; }
  .trim-edge { fill: var(--paper); stroke: var(--trim); stroke-width: 1; }
  .phone-frame { fill: var(--frame); }
  .phone-screen { fill: var(--paper); }
  .section-title {
    font-family: "Open Sans", sans-serif;
    font-weight: 700;
    font-size: 33px;
    letter-spacing: 1px;
    fill: var(--ink);
  }
  .service-name {
    font-family: "Open Sans", sans-serif;
    font-weight: 400;
    font-size: 35px;
    fill: var(--ink);
  }
  .service-icon { fill: var(--accent); }
  .service-icon-line { fill: none; stroke: var(--accent); stroke-width: 2.5; stroke-linejoin: miter; }
  .maker-name {
    font-family: "Open Sans", sans-serif;
    font-weight: 700;
    font-size: 19px;
    fill: var(--brand-ink);
  }
  .maker-divider { stroke: var(--brand-ink); stroke-width: 1.5; }
</style>
</head>
<body>
<svg class="print-sheet" viewBox="0 0 1200 804" xmlns="http://www.w3.org/2000/svg">

  <!-- crop marks -->
  <g class="crop-marks">
    <line class="crop-mark" x1="115" y1="0" x2="115" y2="75"/>
    <line class="crop-mark" x1="1085" y1="0" x2="1085" y2="75"/>
    <line class="crop-mark" x1="115" y1="730" x2="115" y2="804"/>
    <line class="crop-mark" x1="1085" y1="730" x2="1085" y2="804"/>
    <line class="crop-mark" x1="0" y1="127" x2="65" y2="127"/>
    <line class="crop-mark" x1="0" y1="680" x2="65" y2="680"/>
    <line class="crop-mark" x1="1132" y1="127" x2="1200" y2="127"/>
    <line class="crop-mark" x1="1132" y1="680" x2="1200" y2="680"/>
  </g>

  <!-- registration targets -->
  <g class="registration">
    <g transform="translate(600 33)">
      <line class="reg-line" x1="-55" y1="0" x2="55" y2="0"/>
      <line class="reg-line" x1="0" y1="-33" x2="0" y2="33"/>
      <circle class="reg-ring" r="17"/>
      <circle class="reg-dot" r="11"/>
      <line class="reg-cross" x1="-7" y1="-7" x2="7" y2="7"/>
      <line class="reg-cross" x1="7" y1="-7" x2="-7" y2="7"/>
    </g>
    <g transform="translate(30 403)">
      <line class="reg-line" x1="-30" y1="0" x2="28" y2="0"/>
      <line class="reg-line" x1="0" y1="-55" x2="0" y2="55"/>
      <circle class="reg-ring" r="17"/>
      <circle class="reg-dot" r="11"/>
      <line class="reg-cross" x1="-7" y1="-7" x2="7" y2="7"/>
      <line class="reg-cross" x1="7" y1="-7" x2="-7" y2="7"/>
    </g>
    <g transform="translate(1166 403)">
      <line class="reg-line" x1="-24" y1="0" x2="34" y2="0"/>
      <line class="reg-line" x1="0" y1="-55" x2="0" y2="55"/>
      <circle class="reg-ring" r="17"/>
      <circle class="reg-dot" r="11"/>
      <line class="reg-cross" x1="-7" y1="-7" x2="7" y2="7"/>
      <line class="reg-cross" x1="7" y1="-7" x2="-7" y2="7"/>
    </g>
  </g>

  <!-- card trim and phone body -->
  <rect class="trim-edge" x="77" y="89" width="1045" height="628"/>
  <rect class="phone-frame" x="77" y="89" width="1045" height="628" rx="92" ry="92"/>
  <rect class="phone-screen" x="142" y="124" width="916" height="560" rx="72" ry="72"/>

  <!-- services list (reads bottom to top) -->
  <g class="services">
    <text class="section-title" transform="translate(246 502) rotate(-90)">SERVICES</text>

    <text class="service-name" transform="translate(352 568) rotate(-90)">Cracked Screen</text>
    <text class="service-name" transform="translate(446 568) rotate(-90)">Water Damage</text>
    <text class="service-name" transform="translate(539 568) rotate(-90)">Charging Port</text>
    <text class="service-name" transform="translate(632 568) rotate(-90)">Quorvex Data Recovery</text>
    <text class="service-name" transform="translate(726 568) rotate(-90)">Cell Phone Unlock</text>
    <text class="service-name" transform="translate(819 568) rotate(-90)">Tekvo Repair</text>
  </g>

  <!-- service icons -->
  <g class="service-icons">
    <!-- crack -->
    <polyline class="service-icon-line" points="325,619 332,624 336,617 341,626 346,616 351,625 356,619 365,624"/>
    <!-- droplet -->
    <path class="service-icon" d="M414 621 Q438 608 450 612 Q460 621 450 630 Q438 634 414 621 Z"/>
    <!-- lightning -->
    <path class="service-icon" d="M503 604 L530 618 L527 623 L556 637 L524 627 L527 622 Z"/>
    <!-- data cylinder -->
    <g class="service-icon">
      <rect x="602" y="608" width="36" height="26" rx="4"/>
      <rect x="598" y="613" width="4" height="16" rx="2"/>
      <rect x="638" y="613" width="4" height="16" rx="2"/>
    </g>
    <!-- padlock -->
    <g>
      <path class="service-icon" d="M690 612 h30 a6 6 0 0 1 6 6 v16 a6 6 0 0 1 -6 6 h-30 z"/>
      <path class="service-icon-line" d="M726 616 h4 a6 6 0 0 0 0 -12 h-0" style="stroke-width:4"/>
      <circle cx="708" cy="626" r="3" fill="#ffffff"/>
    </g>
    <!-- phone -->
    <g>
      <rect class="service-icon" x="782" y="606" width="48" height="28" rx="5"/>
      <rect x="789" y="610" width="33" height="20" fill="#ffffff"/>
      <rect class="service-icon" x="791" y="612" width="29" height="16"/>
    </g>
  </g>

  <!-- manufacturer names -->
  <g class="makers">
    <text class="maker-name" transform="translate(961 640) rotate(-90)" text-anchor="middle">tekvo</text>
    <line class="maker-divider" x1="938" y1="600" x2="962" y2="600"/>
    <text class="maker-name" transform="translate(961 522) rotate(-90)" text-anchor="middle">velorin</text>
    <line class="maker-divider" x1="938" y1="440" x2="962" y2="440"/>
    <text class="maker-name" transform="translate(961 392) rotate(-90)" text-anchor="middle">kestrin</text>
    <line class="maker-divider" x1="938" y1="345" x2="962" y2="345"/>
    <text class="maker-name" transform="translate(961 296) rotate(-90)" text-anchor="middle">dunbelio</text>
    <line class="maker-divider" x1="938" y1="250" x2="962" y2="250"/>
    <text class="maker-name" transform="translate(961 182) rotate(-90)" text-anchor="middle">orvan</text>
  </g>

</svg>
</body>
</html>
```